I've recently started my own party promotion business. We are currently based in Sydney, Australia. Thus, most of our events are based in the Sydney Metropolitan area, with an eye to continue expanding our business and promote parties right through the Asia Pacific region.

Company details are as follows;

*Company name - Bostrane Promotions
*Company motto - The Velvet Night Hosts
*Website - www.bostrane-example.com
*Phone number - 0455 026 374
*Employee Name - Mick Orandy
*Employee Title - Executive Chief of Operations - Asia Pacific

We need the following items/templates designed;

1. Business Cards
2. Letterhead
3. Envelopes
4. Envelope seals/stickers

At the moment, I am using my mobile number as the main point of contact, for any enquiries. Thus I don't have a landline or fax number. I don't have my 'www.bostrane-example.com' website up and running yet either. Therefore, I would like the templates/designs provided to allow me to add those details at a later date, with ease.

1. Business card.
Note: Please be aware that the design provided will also act as a template to use for any future employees I take on board. Therefore I need to be able to edit the name, title and mobile number with ease.
A. Front Side. I would like my logo to be on the left with the company name to the right of the logo, along the top of the business card. With our company motto directly underneath. Then my name, title, mobile phone number and website following beneath.
B. On the reverse side of the card, I would like the full logo to be centred, with the motto underneath. I want both sides to be royal purple, with everything in glittering gold, consistent with my logo.

2. Letterhead.
A. I would like the full logo to be based to the top right hand corner. With the company motto following underneath.
B. Followed by three lines/spaces to add an address, phone number and fax number, when it becomes applicable. I want these details to be in gold without the purple background. Remembering I need to be able to edit these details when they become available.
C. I would like the website to be emblazoned in gold along the bottom, with the logo on each side of the website address. I also want these details to be in gold without the purple background.

3. Envelopes
Please use your creative expression for this particular template, so as long as it has a consistent matching feel with the Letterhead.

4. Envelope Seals/Stickers
Again, feel free to use your creative flair, so long as it's consistent with the other items. However, I would like these to be round. With only the logo included on the purple background.

If there are any questions, please call me on my mobile number. 0455 026 374.

Many thanks.

Mick

```html
<!DOCTYPE html>
<html lang="en">
<head>
<meta charset="utf-8">
<title>Bostrane Promotions – Stationery</title>
<link href="https://fonts.googleapis.com/css2?family=Questrial&display=swap" rel="stylesheet">
<style>
  :root {
    --purple: #4f2468;
    --purple-deep: #43195b;
    --gold: #d6a52c;
    --gold-light: #f2dc4a;
    --gold-dark: #cf8f2a;
    --paper: #ffffff;
    --ink-grey: #6c6c6c;
    --backdrop: #8a8a8a;
  }
  * { box-sizing: border-box; margin: 0; padding: 0; }
  html, body { width: 1200px; height: 1000px; overflow: hidden; }
  body {
    background: var(--backdrop);
    font-family: "Questrial", "Helvetica Neue", Arial, sans-serif;
    position: relative;
  }
  .sheet { position: absolute; background: var(--paper); overflow: hidden; }
  .shape { position: absolute; left: 0; top: 0; }
  .gold-band {
    position: absolute; left: 0; right: 0;
    background: linear-gradient(90deg, var(--gold-light), var(--gold-dark) 50%, var(--gold-light));
  }
  .brand { display: flex; align-items: center; gap: 8px; color: var(--gold); white-space: nowrap; }
  .brand-dot { border-radius: 50%; background: var(--gold); flex: none; }
  .brand-name { font-weight: 400; letter-spacing: 0.04em; }
  .motto { color: #fff; white-space: nowrap; }

  /* Letterhead */
  .letterhead { left: 27px; top: 66px; width: 620px; height: 870px; }
  .letterhead .contact-line {
    position: absolute; right: 222px; top: 28px;
    font-size: 8.5px; color: var(--ink-grey); display: flex; gap: 8px;
  }
  .contact-line span { display: inline-flex; align-items: center; gap: 3px; }
  .icon { width: 7px; height: 7px; fill: var(--gold); }
  .letterhead .brand { position: absolute; left: 470px; top: 28px; }
  .letterhead .brand-dot { width: 24px; height: 24px; }
  .letterhead .brand-name { font-size: 10px; }
  .letterhead .motto { position: absolute; right: 28px; top: 76px; font-size: 11.5px; }
  .letterhead .footer {
    position: absolute; left: 0; right: 0; bottom: 18px;
    display: flex; justify-content: center; align-items: center; gap: 48px;
  }
  .footer .brand-dot { width: 24px; height: 24px; }
  .footer .web { color: var(--gold); font-size: 10.5px; }
  .letterhead .gold-band { bottom: 0; height: 10px; }

  /* Envelope */
  .envelope { left: 420px; top: 160px; width: 740px; height: 340px; box-shadow: 4px 6px 12px rgba(0,0,0,.35); }
  .envelope .brand { position: absolute; left: 52px; top: 52px; }
  .envelope .brand-dot { width: 30px; height: 30px; }
  .envelope .brand-name { font-size: 12px; }
  .envelope .motto { position: absolute; left: 56px; top: 104px; font-size: 11.5px; }
  .envelope .address {
    position: absolute; left: 60px; top: 140px; font-size: 8.5px; line-height: 1.25; color: var(--purple);
  }
  .envelope .address .row { display: flex; align-items: center; gap: 3px; color: var(--ink-grey); }
  .envelope .gold-band { bottom: 18px; height: 7px; }

  /* Business cards */
  .card { left: 743px; width: 381px; height: 235px; box-shadow: 3px 4px 8px rgba(0,0,0,.3); }
  .card-front { top: 445px; }
  .card-front .top { position: absolute; left: 0; right: 0; top: 0; height: 158px; background: var(--purple); }
  .card-front .brand { position: absolute; left: 80px; top: 40px; }
  .card-front .brand-dot { width: 70px; height: 70px; }
  .card-front .brand-name { font-size: 18px; }
  .card-front .motto { position: absolute; left: 0; right: 0; top: 128px; text-align: center; font-size: 17px; }
  .card-front .person { position: absolute; left: 45px; top: 172px; }
  .person .name { color: var(--purple); font-size: 18px; }
  .person .title { color: var(--ink-grey); font-size: 8.5px; margin-top: 2px; }
  .card-front .details {
    position: absolute; left: 255px; top: 170px; padding-left: 8px;
    border-left: 1px solid #999; font-size: 9.5px; line-height: 1.25; color: var(--ink-grey);
  }
  .details .row { display: flex; align-items: center; gap: 4px; }
  .details .icon { fill: var(--purple); }

  .card-back { top: 702px; background: var(--purple); }
  .card-back .stack { position: absolute; left: 0; right: 0; top: 34px; display: flex; flex-direction: column; align-items: center; gap: 10px; }
  .card-back .brand-dot { width: 80px; height: 80px; }
  .card-back .brand-name { color: var(--gold); font-size: 22px; letter-spacing: 0.06em; }
  .card-back .motto { font-size: 16px; }
</style>
</head>
<body>

<svg width="0" height="0" style="position:absolute">
  <symbol id="i-phone" viewBox="0 0 10 10"><path d="M2 0.5 L3.6 2.8 L2.8 3.8 Q4 6.2 6.2 7.2 L7.2 6.4 L9.5 8 L8.4 9.6 Q3.8 9.4 0.5 1.6 Z"/></symbol>
  <symbol id="i-mobile" viewBox="0 0 10 10"><rect x="2.5" y="0.5" width="5" height="9" rx="1"/></symbol>
  <symbol id="i-globe" viewBox="0 0 10 10"><circle cx="5" cy="5" r="4.5"/></symbol>
</svg>

<!-- Letterhead -->
<section class="sheet letterhead">
  <svg class="shape" width="620" height="100" viewBox="0 0 620 100">
    <rect x="0" y="14" width="620" height="6" fill="var(--purple)"/>
    <polygon points="408,14 620,14 620,92 440,92" fill="var(--purple)"/>
  </svg>
  <div class="contact-line">
    <span>7/48 Marlow Lane, PO BOX 3131, City</span>
    <span><svg class="icon"><use href="#i-phone"/></svg>0455 026 374</span>
    <span><svg class="icon"><use href="#i-mobile"/></svg>0455 026 374</span>
  </div>
  <div class="brand"><span class="brand-dot"></span><span class="brand-name">Bostrane Promotions</span></div>
  <div class="motto">The Velvet Night Hosts</div>
  <div class="footer">
    <span class="brand-dot"></span>
    <span class="web">www.bostrane-example.com</span>
    <span class="brand-dot"></span>
  </div>
  <div class="gold-band"></div>
</section>

<!-- Envelope -->
<section class="sheet envelope">
  <svg class="shape" width="740" height="140" viewBox="0 0 740 140">
    <rect x="0" y="22" width="740" height="10" fill="var(--purple)"/>
    <polygon points="0,30 232,22 212,125 0,132" fill="var(--purple)"/>
  </svg>
  <div class="brand"><span class="brand-dot"></span><span class="brand-name">Bostrane Promotions</span></div>
  <div class="motto">The Velvet Night Hosts</div>
  <div class="address">
    <div class="row"><svg class="icon"><use href="#i-phone"/></svg>0455 026 374</div>
    <div class="row"><svg class="icon"><use href="#i-mobile"/></svg>0455 026 374</div>
    <div>7/48 Marlow Lane, PO BOX 3131,</div>
    <div>City Name, Country</div>
  </div>
  <div class="gold-band"></div>
</section>

<!-- Business card front -->
<section class="sheet card card-front">
  <div class="top"></div>
  <div class="brand"><span class="brand-dot"></span><span class="brand-name">Bostrane Promotions</span></div>
  <div class="motto">The Velvet Night Hosts</div>
  <div class="person">
    <div class="name">Mick Orandy</div>
    <div class="title">Executive Chief of Operations-Asia Pacific</div>
  </div>
  <div class="details">
    <div class="row"><svg class="icon"><use href="#i-mobile"/></svg>0400 000 000</div>
    <div class="row"><svg class="icon"><use href="#i-phone"/></svg>0455 026 374</div>
    <div class="row"><svg class="icon"><use href="#i-globe"/></svg>www.bostrane-example.com</div>
  </div>
</section>

<!-- Business card back -->
<section class="sheet card card-back">
  <div class="stack">
    <span class="brand-dot"></span>
    <span class="brand-name">Bostrane Promotions</span>
    <span class="motto">The Velvet Night Hosts</span>
  </div>
</section>

</body>
</html>
```